plovu business card design

plovu is an incubator within RTM Media focused on unlocking the potential in underserved niche micro-verticals on the web. our mission is to rapidly develop and foster emerging micro-verticals bc they are ripe for growth - building interesting and trusted content experiences with unqiue, useful and cutting-edge delivery methods.please do all copy (except for RTM Media, which must look as typed here and in logo) in all lowercase. Also please use spaces between phone # extensions not dashes or periods. I have attached all variations of the logo.
Industry/Entity Type
Business
Contact Information for Business Card
daria feltow, ceo www.plovu.io 218 holbrook lane 3rd floor oakland ca 94731 415 602 0002m 510 985 7966d daria.feltow@plovu.io
Look and feel
Each slider illustrates characteristics of the customer's brand and the style your logo design should communicate.

```html
<!DOCTYPE html>
<html lang="en">
<head>
<meta charset="utf-8">
<title>plovu business card</title>
<link rel="stylesheet" href="https://fonts.googleapis.com/css2?family=Montserrat:ital,wght@0,400;0,500;0,600;1,400&display=swap">
<style>
  :root {
    --backdrop: #8b8d8c;
    --card-light: #e4e5e7;
    --card-dark: #242223;
    --ink: #1f1d1e;
    --text: #2b2b2b;
    --teal: #128a87;
    --silver: #b9b9bb;
    --white: #ffffff;
  }
  * { margin: 0; padding: 0; box-sizing: border-box; }
  html, body { width: 1200px; height: 900px; overflow: hidden; }
  body {
    background: var(--backdrop);
    font-family: "Montserrat", Arial, sans-serif;
    position: relative;
  }
  .card {
    position: absolute;
    left: 321px;
    width: 507px;
    height: 290px;
    overflow: hidden;
  }
  .card-front { top: 119px; background: var(--card-light); }
  .card-back { top: 471px; background: var(--card-dark); }

  .front-wave { position: absolute; left: 0; top: 0; width: 507px; height: 290px; }

  .brand {
    position: absolute;
    left: 50px;
    top: 100px;
    display: flex;
    flex-direction: column;
  }
  .brand-row { display: flex; align-items: center; gap: 8px; }
  .brand-name {
    font-weight: 600;
    font-size: 56px;
    line-height: 1;
    color: var(--ink);
    letter-spacing: -1px;
  }
  .brand-dot {
    width: 14px; height: 14px; border-radius: 50%;
    background: var(--teal);
    margin-top: 6px;
  }
  .brand-tagline {
    font-size: 11.5px;
    color: var(--text);
    margin-top: 4px;
    margin-left: 2px;
  }

  .divider {
    position: absolute;
    left: 267px; top: 65px;
    width: 1px; height: 141px;
    background: #555;
  }

  .contact { position: absolute; left: 292px; top: 66px; color: var(--text); }
  .contact-name { font-size: 19.5px; font-weight: 500; color: var(--teal); line-height: 1.1; }
  .contact-role { font-size: 14px; margin-top: 3px; }
  .contact-address { font-size: 13px; line-height: 16px; margin-top: 7px; }
  .contact-list { list-style: none; margin-top: 6px; }
  .contact-list li {
    display: flex; align-items: center; gap: 7px;
    font-size: 13px; height: 20px;
  }
  .contact-list svg { width: 13px; height: 13px; flex: none; }

  .splash-area {
    position: absolute;
    left: 441px; top: 234px;
    width: 44px; height: 32px;
    border-radius: 50% 50% 20% 20%;
    background: radial-gradient(circle at 50% 70%, var(--teal) 45%, rgba(18,138,135,0) 75%);
  }

  .front-web {
    position: absolute;
    left: 36px; top: 263px;
    font-size: 12.5px;
    letter-spacing: 3px;
    color: var(--white);
  }

  .back-brand {
    position: absolute;
    left: 0; right: 0; top: 95px;
    text-align: center;
    font-weight: 600;
    font-size: 64px;
    line-height: 1;
    color: var(--silver);
    letter-spacing: -1px;
  }
  .back-web {
    position: absolute;
    left: 0; right: 0; top: 241px;
    text-align: center;
    font-style: italic;
    font-size: 13px;
    letter-spacing: 7px;
    color: var(--white);
  }
</style>
</head>
<body>
  <section class="card card-front" aria-label="business card front">
    <svg class="front-wave" viewBox="0 0 507 290" aria-hidden="true">
      <path d="M0,211 Q170,268 507,265 L507,290 L0,290 Z" fill="var(--teal)"/>
      <path d="M0,228 Q170,280 507,272 L507,290 L0,290 Z" fill="var(--card-dark)" stroke="var(--white)" stroke-width="1.5"/>
    </svg>

    <div class="brand">
      <div class="brand-row">
        <span class="brand-name">plovu</span>
        <span class="brand-dot"></span>
      </div>
      <span class="brand-tagline">an RTM Media incubator</span>
    </div>

    <div class="divider"></div>

    <div class="contact">
      <p class="contact-name">Daria Feltow</p>
      <p class="contact-role">CEO</p>
      <p class="contact-address">218 holbrook lane 3rd floor<br>oakland ca 94731</p>
      <ul class="contact-list">
        <li>
          <svg viewBox="0 0 24 24"><path fill="var(--teal)" d="M6.6 10.8a15.1 15.1 0 0 0 6.6 6.6l2.2-2.2a1 1 0 0 1 1-.25 11.4 11.4 0 0 0 3.6.57 1 1 0 0 1 1 1V20a1 1 0 0 1-1 1A17 17 0 0 1 3 4a1 1 0 0 1 1-1h3.5a1 1 0 0 1 1 1c0 1.25.2 2.45.57 3.57a1 1 0 0 1-.25 1z"/></svg>
          <span>415 738 4196</span>
        </li>
        <li>
          <svg viewBox="0 0 24 24"><rect x="6" y="2" width="12" height="20" rx="2" fill="none" stroke="var(--teal)" stroke-width="2.4"/><circle cx="12" cy="18" r="1.3" fill="var(--teal)"/></svg>
          <span>510 247 3859</span>
        </li>
        <li>
          <svg viewBox="0 0 24 24"><rect x="2" y="6" width="20" height="13" fill="var(--teal)"/><path d="M2 6l10 7 10-7" fill="none" stroke="var(--card-light)" stroke-width="1.6"/></svg>
          <span>daria.feltow@plovu.io</span>
        </li>
      </ul>
    </div>

    <div class="splash-area" role="img" aria-label="teal ink splash decoration"></div>

    <p class="front-web">www.plovu.co</p>
  </section>

  <section class="card card-back" aria-label="business card back">
    <p class="back-brand">plovu</p>
    <p class="back-web">www.plovu.co</p>
  </section>
</body>
</html>
```